Design some Business Cards (project 18 aug)

Please create a business card. You can find the logotype as attachment. The company core business is logotype design.
Size 90 x 55 mm. Please deliver in adobe Illustrator file format (.AI). Use dummy name and contact information.

```html
<!DOCTYPE html>
<html lang="en">
<head>
<meta charset="UTF-8">
<title>Markwell Business Card</title>
<link rel="stylesheet" href="https://fonts.googleapis.com/css2?family=Montserrat:wght@400;600;700;800&display=swap">
<style>
  :root {
    --backdrop: #3a3b3e;
    --card-black: #050505;
    --brand-blue: #3d55a8;
    --brand-red: #e3262c;
    --brand-grey: #b9b9bc;
    --text-white: #ffffff;
    --logo-light: #d6d6d8;
  }
  * { margin: 0; padding: 0; box-sizing: border-box; }
  html, body { width: 1200px; height: 900px; overflow: hidden; }
  body {
    background: var(--backdrop);
    font-family: "Montserrat", sans-serif;
    position: relative;
  }
  .card {
    position: absolute;
    width: 520px;
    height: 318px;
    border-radius: 22px;
    background: var(--card-black);
    overflow: hidden;
  }
  .card-front { left: 130px; top: 110px; }
  .card-back { left: 550px; top: 470px; }

  .brand {
    position: absolute;
    display: flex;
    align-items: center;
    gap: 10px;
    color: var(--logo-light);
    font-weight: 800;
    letter-spacing: -1px;
  }
  .brand-dot {
    border-radius: 50%;
    background: var(--brand-blue);
  }
  .card-front .brand {
    left: 0; right: 0; top: 100px;
    justify-content: center;
    font-size: 64px;
  }
  .card-front .brand-dot { width: 22px; height: 22px; }
  .front-web {
    position: absolute;
    left: 0; right: 0; bottom: 40px;
    text-align: center;
    color: var(--text-white);
    font-size: 12px;
    font-weight: 700;
  }
  .front-web .accent { color: var(--brand-red); }

  .card-back .brand {
    right: 40px; top: 54px;
    font-size: 44px;
  }
  .card-back .brand-dot { width: 16px; height: 16px; }

  .card-waves { position: absolute; inset: 0; }

  .person {
    position: absolute;
    left: 18px; top: 96px;
    width: 130px;
    border-bottom: 3px solid var(--brand-grey);
    padding-bottom: 3px;
  }
  .person-name {
    color: var(--brand-red);
    font-size: 15px;
    font-weight: 600;
  }
  .person-role {
    color: var(--text-white);
    font-size: 11px;
    font-weight: 400;
  }

  .contacts {
    position: absolute;
    left: 18px; bottom: 14px;
    list-style: none;
    color: var(--text-white);
    font-size: 11px;
    font-weight: 400;
  }
  .contacts li {
    display: flex;
    align-items: center;
    gap: 8px;
    height: 19px;
  }
  .contacts li:first-child { font-size: 13px; }
  .contact-icon { width: 12px; height: 12px; flex: none; }
</style>
</head>
<body>

  <section class="card card-front">
    <div class="brand"><span class="brand-name">Markwell</span><span class="brand-dot"></span></div>
    <p class="front-web">www.<span class="accent">markwell</span>.com</p>
  </section>

  <section class="card card-back">
    <svg class="card-waves" width="520" height="318" viewBox="0 0 520 318">
      <path fill="var(--brand-red)" d="M0,238 C110,176 220,158 330,160 L330,172 C220,172 115,196 0,258 Z"/>
      <path fill="var(--brand-grey)" d="M320,174 C410,176 470,150 520,100 L520,122 C470,165 410,182 320,178 Z"/>
      <path fill="var(--brand-blue)" d="M0,256 C115,196 220,174 320,176 C410,178 470,158 520,120 L520,318 L0,318 Z"/>
    </svg>

    <div class="brand"><span class="brand-name">Markwell</span><span class="brand-dot"></span></div>

    <div class="person">
      <p class="person-name">Dana Hollis</p>
      <p class="person-role">Physiotherapist</p>
    </div>

    <ul class="contacts">
      <li>
        <svg class="contact-icon" viewBox="0 0 12 12"><path fill="var(--brand-red)" d="M2.5,1 L4.5,1 L5.2,3.6 L4,4.6 C4.7,6 6,7.3 7.4,8 L8.4,6.8 L11,7.5 L11,9.5 C11,10.3 10.3,11 9.5,11 C5,11 1,7 1,2.5 C1,1.7 1.7,1 2.5,1 Z"/></svg>
        0400555019
      </li>
      <li>
        <svg class="contact-icon" viewBox="0 0 12 12"><circle cx="6" cy="6" r="6" fill="var(--brand-red)"/><rect x="2.5" y="3.8" width="7" height="4.6" fill="none" stroke="#fff" stroke-width="0.9"/><path d="M2.5,3.8 L6,6.5 L9.5,3.8" fill="none" stroke="#fff" stroke-width="0.9"/></svg>
        info@northbaydesignstudioandprint.com.au
      </li>
      <li>
        <svg class="contact-icon" viewBox="0 0 12 12"><circle cx="6" cy="6" r="5" fill="none" stroke="var(--brand-red)" stroke-width="1.2"/><ellipse cx="6" cy="6" rx="2" ry="5" fill="none" stroke="var(--brand-red)" stroke-width="1"/><line x1="1" y1="6" x2="11" y2="6" stroke="var(--brand-red)" stroke-width="1"/></svg>
        www.northbaydesignstudioandprint.com.au
      </li>
    </ul>
  </section>

</body>
</html>
```